Single brochure for international companies in the financial sector

We need to update a brochure 4 pages presenting our company. We are a financial engineering company. The final design must provide financial security, service and trust. you will find the current brochure copy. Our color code is Orange (RGB 235/100/68), Black, White and Gray. photos show the visual of the site, but it is not mandatory to keep them.

Target Market(s)

wealth management professionals

Industry/Entity Type

Finance

Requirements
Must have
• Logo Tolvane Capital all text in the document color Orange Tolvane (RGB 235/100/68)
Nice to have
• Vista Font
Should not have
• images / pictures of people

```html
<!DOCTYPE html>
<html lang="en">
<head>
<meta charset="utf-8">
<title>Tolvane Capital – Brochure</title>
<link href="https://fonts.googleapis.com/css2?family=Questrial&display=swap" rel="stylesheet">
<style>
  :root{
    --orange:#eb6444;
    --navy:#2f4562;
    --navy-deep:#22344c;
    --sky:#4f8cc4;
    --sea:#2f6f86;
    --text:#666a70;
    --white:#ffffff;
    --paper:#f7f7f7;
    --bg:#dcdcdc;
  }
  *{box-sizing:border-box;margin:0;padding:0}
  html,body{width:1200px;height:3846px;overflow:hidden}
  body{background:var(--bg);font-family:"Questrial",sans-serif;color:var(--text);position:relative}
  .spread{position:absolute;left:50px;width:1100px;height:870px;background:var(--white);box-shadow:0 6px 18px rgba(0,0,0,.18);overflow:hidden}
  .spread--outer{top:990px}
  .spread--inner{top:1980px}
  .spread svg.shapes{position:absolute;inset:0;width:1100px;height:870px}
  .fold{position:absolute;left:549px;top:0;width:2px;height:870px;background:linear-gradient(90deg,rgba(0,0,0,.08),rgba(0,0,0,0))}
  .abs{position:absolute}

  /* outer spread */
  .brand{left:550px;width:550px;top:72px;text-align:center;color:var(--orange)}
  .brand__mark{display:inline-block;width:14px;height:14px;background:var(--orange);margin-bottom:10px}
  .brand__name{font-size:34px;letter-spacing:12px;line-height:1}
  .brand__sub{font-size:15px;letter-spacing:7px;margin-top:8px}
  .cover-title{right:40px;top:420px;text-align:right;color:var(--white);font-size:33px;line-height:1.18;letter-spacing:1px}
  .website{width:550px;top:790px;text-align:center;font-size:13px;letter-spacing:4px;color:#9a9a9a}
  .website--back{left:0}
  .website--front{left:550px}
  .contact{left:0;width:550px;top:270px;text-align:center;color:rgba(255,255,255,.78)}
  .contact__name{font-size:22px;letter-spacing:9px}
  .contact__sub{font-size:11px;letter-spacing:5px;margin-top:5px}
  .contact__lines{margin-top:28px;font-size:11px;line-height:1.7;letter-spacing:1px}
  .contact__lines p+p{margin-top:2px}
  .contact__gap{margin-top:18px}

  /* inner spread */
  .band-title{top:248px;color:var(--white);font-size:30px;letter-spacing:1px}
  .band-title--company{left:40px}
  .band-title--services{left:690px}
  .column{width:470px}
  .column--left{left:40px;top:360px}
  .column--right{left:600px;top:345px}
  .section+.section{margin-top:14px}
  .section h3{display:flex;align-items:center;gap:8px;color:var(--orange);font-size:19px;font-weight:400;margin-bottom:5px}
  .section h3 svg{width:16px;height:16px;flex:none}
  .section p{font-size:13.5px;line-height:1.42}
  .section p+p{margin-top:7px}
  .quote{left:600px;top:806px;width:470px;text-align:center;color:var(--white);font-size:13.5px;line-height:1.45;font-style:italic}
</style>
</head>
<body>

<!-- Outer spread: back cover + front cover -->
<section class="spread spread--outer">
  <svg class="shapes" viewBox="0 0 1100 870" aria-hidden="false">
    <defs>
      <linearGradient id="coverPhoto" x1="0" y1="0" x2="0" y2="1">
        <stop offset="0" stop-color="#7fb0dc"/>
        <stop offset=".45" stop-color="var(--sky)"/>
        <stop offset=".75" stop-color="var(--sea)"/>
        <stop offset="1" stop-color="#1f5564"/>
      </linearGradient>
      <linearGradient id="backPhoto" x1="0" y1="0" x2="0" y2="1">
        <stop offset="0" stop-color="#3a5270"/>
        <stop offset="1" stop-color="var(--navy-deep)"/>
      </linearGradient>
    </defs>
    <path role="img" aria-label="Muted navy photo of a suspension bridge over a bay"
          d="M0,150 C160,150 360,200 550,232 L550,640 C360,662 160,652 0,618 Z" fill="url(#backPhoto)"/>
    <path d="M0,134 C160,134 360,184 550,216" fill="none" stroke="var(--orange)" stroke-width="5"/>
    <path d="M0,636 C160,670 360,680 550,658" fill="none" stroke="var(--orange)" stroke-width="5"/>

    <path role="img" aria-label="Photo of a red suspension bridge over a blue bay under a clear sky"
          d="M550,232 C740,200 940,150 1100,150 L1100,618 C940,652 740,662 550,640 Z" fill="url(#coverPhoto)"/>
    <path d="M550,216 C740,184 940,134 1100,134" fill="none" stroke="var(--orange)" stroke-width="5"/>
    <path d="M550,658 C740,680 940,670 1100,636" fill="none" stroke="var(--orange)" stroke-width="5"/>
  </svg>
  <div class="fold"></div>

  <div class="abs contact">
    <div class="contact__name">TOLVANE</div>
    <div class="contact__sub">CAPITAL</div>
    <div class="contact__lines">
      <p>00 RUE DES LILAS 75000 PARIS</p>
      <p class="contact__gap">Tolvane Capital S.A.S.</p>
      <p>Capital 100 000 €</p>
      <p>RCS Paris 000 000 000</p>
      <p class="contact__gap">+33 1 00 00 00 00</p>
      <p class="contact__gap">contact@tolvanecapital.com</p>
    </div>
  </div>
  <div class="abs website website--back">www.tolvanecapital.com</div>

  <div class="abs brand">
    <span class="brand__mark"></span>
    <div class="brand__name">TOLVANE</div>
    <div class="brand__sub">CAPITAL</div>
  </div>
  <div class="abs cover-title">FINANCIAL<br>ENGINEERING</div>
  <div class="abs website website--front">www.tolvanecapital.com</div>
</section>

<!-- Inner spread: company + services -->
<section class="spread spread--inner">
  <svg class="shapes" viewBox="0 0 1100 870">
    <defs>
      <linearGradient id="bandPhoto" x1="0" y1="0" x2="0" y2="1">
        <stop offset="0" stop-color="#3e5877"/>
        <stop offset="1" stop-color="var(--navy)"/>
      </linearGradient>
      <linearGradient id="railPhoto" x1="0" y1="0" x2="0" y2="1">
        <stop offset="0" stop-color="#ffffff"/>
        <stop offset=".35" stop-color="#c9cbcf"/>
        <stop offset="1" stop-color="#8a8d92"/>
      </linearGradient>
    </defs>
    <path role="img" aria-label="Navy-toned photo of a suspension bridge across a bay"
          d="M0,0 H1100 V292 C820,262 320,348 0,300 Z" fill="url(#bandPhoto)"/>
    <path d="M0,300 C320,348 820,262 1100,292 V318 C820,290 320,372 0,326 Z" fill="var(--orange)"/>
    <path role="img" aria-label="Grey photo of cobblestone street with tram rails"
          d="M0,600 H550 V870 H0 Z" fill="url(#railPhoto)"/>
    <path d="M550,792 C760,760 930,774 1100,740 V870 H550 Z" fill="var(--orange)"/>
  </svg>
  <div class="fold"></div>

  <div class="abs band-title band-title--company">THE COMPANY</div>
  <div class="abs band-title band-title--services">OUR SERVICES</div>

  <div class="abs column column--left">
    <div class="section">
      <h3><svg viewBox="0 0 16 16"><rect x="1" y="6" width="4" height="9" fill="var(--orange)"/><rect x="6" y="2" width="4" height="13" fill="var(--orange)"/><rect x="11" y="8" width="4" height="7" fill="var(--orange)"/></svg>About Us</h3>
      <p>Tolvane Capital is a financial engineering company.<br>It's fully independent from any bank or any other company.</p>
    </div>
    <div class="section">
      <h3><svg viewBox="0 0 16 16"><circle cx="8" cy="5" r="3.5" fill="var(--orange)"/><path d="M1,15 C2,9 14,9 15,15 Z" fill="var(--orange)"/></svg>Our Clients</h3>
      <p>Our clients are financial professionals such as asset managers, institutionals, corporates, private banks, wealth managers and family offices.</p>
      <p>Our purpose is to make their work easier, every day.</p>
    </div>
    <div class="section">
      <h3><svg viewBox="0 0 16 16"><path d="M2,8 L6,12 L14,3" fill="none" stroke="var(--orange)" stroke-width="3"/></svg>What we do</h3>
      <p>We provide them with investment solutions designed to improve their portfolios performance.</p>
      <p>Simple as that.</p>
    </div>
  </div>

  <div class="abs column column--right">
    <div class="section">
      <h3><svg viewBox="0 0 16 16"><rect x="1" y="1" width="14" height="14" fill="var(--orange)"/><path d="M4,11 L7,7 L9,9 L12,5" fill="none" stroke="#fff" stroke-width="1.6"/></svg>Investment Advice</h3>
      <p>Each client is looking for a unique investment solution. Hence, we combine internal and external resources to create the financial product that will best fit our clients requirements.</p>
      <p>Thanks to a truly independent advice, we offer bespoke, simple and efficient solutions.</p>
    </div>
    <div class="section">
      <h3><svg viewBox="0 0 16 16"><path d="M8,8 L8,1 A7,7 0 1 1 1,8 Z" fill="var(--orange)"/><path d="M7,7 L7,1 A6,6 0 0 0 1,7 Z" fill="var(--orange)" opacity=".6"/></svg>Portfolio Analysis</h3>
      <p>We advise our clients on their portfolios of financial products. Together we identify the needs for restructuring or reallocating the assets.</p>
      <p>We also provide full monitoring and reporting services throughout the life of the products.</p>
    </div>
    <div class="section">
      <h3><svg viewBox="0 0 16 16"><circle cx="5" cy="6" r="3" fill="var(--orange)"/><circle cx="11" cy="6" r="3" fill="var(--orange)"/><rect x="1" y="10" width="14" height="5" fill="var(--orange)"/></svg>Partner Selection</h3>
      <p>Our internal tools allow us to continuously assess the issuers we are working with.</p>
      <p>Therefore we give our clients the luxury to chose among the best issuers for their investment solution.</p>
    </div>
  </div>

  <div class="abs quote">“Our clients must deliver performance on their portfolios on a regular basis.<br>We help them deliver everyday.”</div>
</section>

</body>
</html>
```